Holistic Psychologist needs contemporary business card

I am a psychologist working with adult clients face to face and online. The card needs to work for clients and also referring doctors and medical professionals. It needs to look warm, safe and trustable for clients, but clean and professional enough for doctors. Sometimes I also work in a corporate context.

I am holistic in my approach (mind-body-spirit) so anything conveying connection or integration or wholeness would be good. But again, clean and contemporary please. It can have a little bit of personality.
New logo uploaded.

Probably warm tones and plenty white space to write on one side.

My web pages:
http://lmtherapy.com.au
https://www.facebook.com/MarcellaWhitfordTherapy?ref=hl
Updates

Hi Designers .. I have decided I do need a new logo before finalising a design for the business cards.  I hope to have this available in 4 days from now.

Kindly,

Marcella

New logo now posted, same brief.  Balance of masculine and feminine elements, plenty of white space on one side please.

Keen to see some card designs, thank-you.

Target Market(s)

Audience 1 - Males and females aged 25 years + seeking counselling or coaching. Audience 2 - doctors and health professionals who refer clients.

Industry/Entity Type

Medical

Contact Information for Business Card

Logo

Marcella Whitford
Registered Psychologist

M: 0491 508 243
www.lmtherapy.com.au
marcella@lmtherapy.com.au
Little blue Facebook icon, with "marcella whitford therapy" printed near it.

Font styles to use
Sans Serif

Requirements
Nice to have
• You might want to play with the words "essential you"
Should not have
• Nothing cutesy or too literal

```html
<!DOCTYPE html>
<html lang="en">
<head>
<meta charset="utf-8">
<title>Marcella Whitford Therapy – Business Card</title>
<link rel="stylesheet" href="https://fonts.googleapis.com/css2?family=Poiret+One&family=PT+Sans+Narrow:wght@400;700&display=swap">
<style>
  :root {
    --card-bg: #f8f2eb;
    --brand-red: #e4452c;
    --band-red: #e4452c;
    --ink-white: #ffffff;
    --ink-warm: #4a3c34;
    --key-dark: #5a2a20;
    --social-blue: #4a67b0;
  }
  html, body {
    margin: 0;
    padding: 0;
    width: 1200px;
    height: 720px;
    overflow: hidden;
    background: var(--card-bg);
  }
  .card {
    position: relative;
    width: 1200px;
    height: 720px;
    background: var(--card-bg);
    overflow: hidden;
  }
  .brand {
    position: absolute;
    left: 228px;
    top: 168px;
    display: flex;
    align-items: center;
    gap: 40px;
  }
  .brand-dot {
    width: 120px;
    height: 120px;
    border-radius: 50%;
    background: var(--brand-red);
    flex: none;
  }
  .brand-name {
    font-family: "Poiret One", sans-serif;
    font-size: 50px;
    line-height: 1;
    color: var(--brand-red);
    white-space: nowrap;
  }
  .red-band {
    position: absolute;
    left: 0;
    top: 334px;
    width: 1200px;
    height: 276px;
  }
  .red-band path { fill: var(--band-red); }
  .practitioner {
    position: absolute;
    left: 122px;
    top: 414px;
    color: var(--ink-white);
    font-family: "Poiret One", sans-serif;
  }
  .practitioner-name {
    font-size: 40px;
    line-height: 1;
    margin: 0;
    font-weight: 400;
  }
  .practitioner-title {
    font-size: 22px;
    line-height: 1;
    margin: 6px 0 0;
  }
  .contacts {
    position: absolute;
    right: 123px;
    top: 416px;
    margin: 0;
    padding: 0;
    list-style: none;
    text-align: right;
    font-family: "PT Sans Narrow", sans-serif;
    font-size: 26px;
    line-height: 40px;
    color: var(--ink-white);
  }
  .contact-key {
    margin-right: 18px;
    font-weight: 700;
  }
  .contact-key b {
    color: var(--key-dark);
    padding: 0 5px;
  }
  .social {
    position: absolute;
    left: 408px;
    top: 597px;
    display: flex;
    align-items: center;
    gap: 24px;
    font-family: "PT Sans Narrow", sans-serif;
    font-size: 26px;
    color: var(--ink-warm);
    text-transform: uppercase;
  }
  .social-square {
    width: 38px;
    height: 38px;
    background: var(--social-blue);
    flex: none;
  }
</style>
</head>
<body>
<main class="card">
  <div class="brand">
    <span class="brand-dot"></span>
    <span class="brand-name">Marcella Whitford Therapy</span>
  </div>

  <svg class="red-band" viewBox="0 0 1200 276" preserveAspectRatio="none" aria-hidden="true">
    <path d="M0 12 L14 8 L26 13 L40 9 L56 14 L70 10 L86 13 L102 7 L118 12 L134 9 L150 14 L168 8 L184 12 L200 9 L218 13 L236 8 L252 12 L270 10 L288 14 L306 8 L324 11 L342 9 L360 13 L380 7 L398 12 L416 9 L436 13 L456 8 L474 11 L494 9 L514 13 L534 7 L554 11 L574 8 L594 12 L614 7 L634 10 L654 8 L674 12 L694 6 L714 10 L734 7 L754 11 L776 5 L796 9 L816 6 L838 10 L860 4 L880 8 L902 5 L924 9 L946 3 L966 7 L988 4 L1010 8 L1032 2 L1054 6 L1076 3 L1098 7 L1120 2 L1142 5 L1164 1 L1184 4 L1200 2
             L1200 238 L1184 242 L1168 237 L1150 243 L1132 239 L1114 245 L1096 240 L1078 246 L1060 241 L1040 247 L1020 242 L1000 248 L980 243 L960 249 L940 244 L918 250 L898 246 L876 252 L856 247 L834 253 L812 248 L790 254 L768 250 L746 256 L724 251 L702 257 L680 252 L658 258 L636 254 L614 259 L592 255 L570 261 L548 256 L526 262 L504 257 L482 263 L460 258 L438 264 L416 259 L394 265 L372 260 L350 266 L328 261 L306 267 L284 262 L262 268 L240 263 L218 269 L196 264 L174 270 L152 265 L130 271 L108 266 L86 272 L64 267 L42 273 L20 268 L0 272 Z"/>
  </svg>

  <div class="practitioner">
    <h1 class="practitioner-name">Marcella Whitford</h1>
    <p class="practitioner-title">REGISTERED PSYCHOLOGIST</p>
  </div>

  <ul class="contacts">
    <li><span class="contact-key">{<b>M</b>}</span>0491 508 243</li>
    <li><span class="contact-key">{<b>E</b>}</span>marcella@lmtherapy.com.au</li>
    <li><span class="contact-key">{<b>W</b>}</span>www.lmtherapy.com.au</li>
  </ul>

  <div class="social">
    <span class="social-square"></span>
    <span class="social-handle">Marcella Whitford Therapy</span>
  </div>
</main>
</body>
</html>
```